RWP Tax Services
RWP Tax Services -
Creative Brief
Professional
Dan Feltwicke
President
2847 Harbor Street, Suite 210 San Jose, CA 95128
dan@rwptaxdemo.com
www.rwptaxdemo.com
We want the card to look and feel like it is a combination of real estate business card and CPA business card. Tax professional (CPA office) with photo (real estate business) of president.

```html
<!DOCTYPE html>
<html lang="en">
<head>
<meta charset="utf-8">
<title>RWP Tax Services – Business Card</title>
<link href="https://fonts.googleapis.com/css2?family=Questrial&display=swap" rel="stylesheet">
<style>
  :root {
    --navy: #1f4f97;
    --navy-light: #3f6cb0;
    --orange: #e0892a;
    --ink: #1c1c1c;
    --paper: #ffffff;
    --edge: #b9b9b9;
    --photo-top: #8a6a55;
    --photo-bottom: #3e3a3c;
  }
  html, body {
    margin: 0;
    padding: 0;
    width: 1200px;
    height: 845px;
    overflow: hidden;
    background: var(--paper);
    font-family: "Questrial", "Century Gothic", sans-serif;
    color: var(--ink);
  }
  .canvas { position: relative; width: 1200px; height: 845px; }

  /* Front side */
  .card-front {
    position: absolute;
    left: 112px; top: 112px;
    width: 533px; height: 306px;
    background: var(--navy);
    overflow: hidden;
  }
  .card-front .brand {
    position: absolute;
    left: 0; right: 0; top: 112px;
    text-align: center;
    color: var(--paper);
    font-size: 34px;
    letter-spacing: 1px;
    line-height: 1;
  }
  .card-front .website {
    position: absolute;
    left: 0; right: 0; top: 205px;
    text-align: center;
    color: var(--paper);
    font-size: 19px;
    line-height: 1;
  }
  .card-front .house-artwork {
    position: absolute;
    left: 0; top: 238px;
    width: 200px; height: 44px;
    background: linear-gradient(180deg, var(--navy), var(--navy-light));
  }
  .card-front .base-band {
    position: absolute;
    left: 0; right: 0; top: 282px;
    height: 7px;
    background: var(--paper);
  }

  /* Back side */
  .card-back {
    position: absolute;
    left: 550px; top: 450px;
    width: 522px; height: 298px;
    background: var(--paper);
    border: 2px solid var(--edge);
  }
  .card-back .accent-bar {
    position: absolute;
    right: -2px; top: 150px;
    width: 14px; height: 72px;
    background: var(--orange);
  }
  .card-back .brand {
    position: absolute;
    left: 22px; top: 70px;
    width: 220px;
    text-align: center;
    color: var(--navy);
    font-size: 24px;
    line-height: 1;
  }
  .card-back .address,
  .card-back .phones {
    position: absolute;
    left: 27px;
    font-size: 13px;
    line-height: 19px;
    letter-spacing: 1px;
  }
  .card-back .address { top: 164px; }
  .card-back .phones { top: 226px; }
  .card-back .portrait {
    position: absolute;
    left: 393px; top: 25px;
    width: 86px; height: 118px;
    background: linear-gradient(180deg, var(--photo-top), var(--photo-bottom));
    border: 1px solid #777;
  }
  .card-back .person {
    position: absolute;
    left: 322px; top: 156px;
    width: 190px;
    text-align: center;
  }
  .card-back .person .name { font-size: 21px; line-height: 24px; }
  .card-back .person .title { font-size: 15px; line-height: 20px; }
  .card-back .online {
    position: absolute;
    left: 292px; top: 226px;
    width: 220px;
    text-align: center;
    font-size: 13px;
    line-height: 19px;
    white-space: nowrap;
  }
</style>
</head>
<body>
<div class="canvas">

  <section class="card-front">
    <div class="brand">RWP Tax Services</div>
    <div class="website">www.rwptaxdemo.com</div>
    <div class="house-artwork" role="img" aria-label="Line drawing of a house roof with chimney"></div>
    <div class="base-band"></div>
  </section>

  <section class="card-back">
    <div class="brand">RWP Tax Services</div>
    <div class="address">2847 Harbor Street, Suite 210<br>San Jose, CA 95128</div>
    <div class="phones">Toll-free (877) 555-0148<br>Phone (408) 555-0162<br>Fax (408) 555-0197</div>
    <div class="portrait" role="img" aria-label="Portrait photograph of the company president"></div>
    <div class="person">
      <div class="name">Dan Feltwicke</div>
      <div class="title">PRESIDENT</div>
    </div>
    <div class="online">Email dan@rwptaxdemo.com<br>www.rwptaxdemo.com</div>
    <div class="accent-bar"></div>
  </section>

</div>
</body>
</html>
```